Tamaru Peruvian Cuisine needs a take-out menu

We need a new tri-fold 8.5"x11" take out menu for a Peruvian restaurant based in New Rochelle, NY. We have a vast selections of dishes from appetizers, seafood based dishes, desserts, Peruvian ceviches and more. We have attached the following:

Restaurant information
Pictures of our dishes
Tamaru Logo in pdf format
Menu in word format
Old take out menu for reference only! (our dishes have changed)
Updates

Project Deadline Extended
Reason: Need more time to make final decision.

Industry/Entity Type

Restaurant

```html
<!DOCTYPE html>
<html lang="en">
<head>
<meta charset="utf-8">
<title>Tamaru Peruvian Cuisine – Take-out Menu (Inside Spread)</title>
<link rel="stylesheet" href="https://fonts.googleapis.com/css2?family=Chewy&family=Cabin+Condensed:wght@600;700&family=Patrick+Hand&display=swap">
<style>
  :root {
    --leaf: #7cc242;
    --leaf-deep: #5fa82e;
    --leaf-light: #8fd255;
    --card: #8b5a43;
    --card-edge: #6e4230;
    --cream: #fff6ea;
    --rule: #ffffff;
    --photo-soup: #d4823a;
    --photo-salad: #c9504f;
    --photo-ceviche: #d9c7b4;
    --photo-seafood: #8a5a3a;
    --photo-chicken: #b86a3a;
    --photo-steak: #7a3b28;
  }
  * { box-sizing: border-box; margin: 0; padding: 0; }
  html, body { width: 1200px; height: 900px; overflow: hidden; background: #ffffff; }

  .menu-spread {
    position: relative;
    width: 1200px; height: 900px;
    background: radial-gradient(ellipse at 55% 45%, var(--leaf-light), var(--leaf) 55%, var(--leaf-deep));
    overflow: hidden;
  }
  .fold { position: absolute; top: 0; bottom: 0; width: 1px; background: rgba(255,255,255,.55); }
  .fold--one { left: 400px; }
  .fold--two { left: 800px; }
  .rule { position: absolute; height: 2px; background: var(--rule); }

  .menu-card {
    position: absolute;
    background: linear-gradient(160deg, #94604a, var(--card) 45%, #7e4f3a);
    border: 1px solid var(--card-edge);
    box-shadow: 2px 3px 6px rgba(0,0,0,.25);
    color: var(--cream);
    padding: 12px 16px;
    overflow: hidden;
  }
  .photo-clearance { float: right; }
  .section-title {
    font-family: "Chewy", "Trebuchet MS", sans-serif;
    font-weight: 400;
    font-size: 22px; line-height: 1.0;
    color: var(--cream);
    margin-bottom: 8px;
    letter-spacing: .4px;
  }
  .dish-name {
    font-family: "Cabin Condensed", "Arial Narrow", sans-serif;
    font-weight: 700; font-size: 10.5px;
    text-transform: uppercase; letter-spacing: .3px;
    line-height: 1.2;
  }
  .dish-desc {
    font-family: "Patrick Hand", "Comic Sans MS", cursive;
    font-size: 11px; line-height: 1.12;
    margin-bottom: 4px;
  }
  .align-right { text-align: right; }
  .title-right { text-align: right; white-space: nowrap; }
  .narrow { width: 56%; }

  .dish-photo {
    position: absolute; border-radius: 50%;
    border: 4px solid #ffffff;
    box-shadow: 0 3px 8px rgba(0,0,0,.3);
  }
  .dish-photo--soup { background: radial-gradient(circle at 45% 45%, #e9a35a, var(--photo-soup) 60%, #a85a2a); }
  .dish-photo--salad { background: radial-gradient(circle at 50% 45%, #e86a6a, var(--photo-salad) 55%, #5a8a3a); }
  .dish-photo--ceviche { background: radial-gradient(circle at 50% 50%, #f2e6d8, var(--photo-ceviche) 60%, #c78a6a); }
  .dish-photo--seafood { background: radial-gradient(circle at 55% 45%, #b07a52, var(--photo-seafood) 60%, #d8d2c4); }
  .dish-photo--chicken { background: radial-gradient(circle at 50% 60%, #d08650, var(--photo-chicken) 55%, #eeeae2); }
  .dish-photo--steak { background: radial-gradient(circle at 50% 50%, #a14a30, var(--photo-steak) 60%, #e8e4d8); }
</style>
</head>
<body>
<main class="menu-spread">
  <div class="fold fold--one"></div>
  <div class="fold fold--two"></div>
  <div class="rule" style="left:0;top:318px;width:400px;"></div>
  <div class="rule" style="left:400px;top:455px;width:400px;"></div>
  <div class="rule" style="left:800px;top:74px;width:400px;"></div>

  <!-- Panel one -->
  <section class="menu-card" style="left:33px;top:22px;width:289px;height:288px;">
    <span class="photo-clearance" style="width:62px;height:112px;"></span>
    <h2 class="section-title">Sopas<br>/Soups</h2>
    <p class="dish-name">Aguadito Limeño</p>
    <p class="dish-desc">chicken and vegetable soup mixed with rice and cilantro<br>Large – $9.95 &nbsp; Small – $5.95</p>
    <p class="dish-name">Sopa a la Minuta</p>
    <p class="dish-desc">traditional milk and angel's hair pasta soup, served with beef and eggs – $12.95</p>
    <p class="dish-name">Caldo de Gallina</p>
    <p class="dish-desc">hen broth with noodles, scallion, potatoes and hard-boiled egg – $12.95</p>
    <p class="dish-name">Chupe de Camarones Arequipeño</p>
    <p class="dish-desc">shrimp soup mixed with rice, green peas, Cusco corn, milk, eggs and Peruvian spices – $15.95</p>
    <p class="dish-name">Parihuela del Puerto</p>
    <p class="dish-desc">classic Peruvian seafood soup – $18.95</p>
  </section>
  <div class="dish-photo dish-photo--soup" role="img" aria-label="Photo of a bowl of Peruvian soup" style="left:258px;top:22px;width:120px;height:120px;"></div>

  <section class="menu-card" style="left:33px;top:326px;width:289px;height:188px;">
    <span class="photo-clearance" style="width:36px;height:96px;"></span>
    <h2 class="section-title">Ensaladas<br>/Salads</h2>
    <p class="dish-name">Ensalada de la Casa</p>
    <p class="dish-desc">lettuce, tomatoes, yellow peppers and choclo – $6.95</p>
    <p class="dish-name">Ensalada Tamaru</p>
    <p class="dish-desc">lettuce, tomatoes, cucumbers, red onions, carrots, radish and avocado – $7.95</p>
    <p class="dish-name">Ensalada Cesar</p>
    <p class="dish-desc">romaine, lettuce, croutons, parmesan cheese and Tamaru's special sauce – $8.95</p>
  </section>
  <div class="dish-photo dish-photo--salad" role="img" aria-label="Photo of a fresh house salad" style="left:282px;top:322px;width:110px;height:110px;"></div>

  <section class="menu-card align-right" style="left:81px;top:522px;width:288px;height:356px;">
    <h2 class="section-title" style="text-align:left;">Ceviche</h2>
    <p class="dish-name">Leche de Tigre</p>
    <p class="dish-desc">ceviche marinade in fresh lime juice – $10.95</p>
    <p class="dish-name">Tiradito en Salsa de Aji Amarillo</p>
    <p class="dish-desc">sashimi style fish in yellow pepper sauce and fresh lime juice, served with Cusco corn and sweet potatoes – $12.95</p>
    <p class="dish-name">Piqueo Chalaco</p>
    <p class="dish-desc">dish combined of Ceviche de Pescado (Fish Ceviche) and Jalea (Fried Seafood) – $24.95</p>
    <div style="padding-left:72px;">
      <p class="dish-name">Ceviche</p>
      <p class="dish-desc">choice of raw fish, mixed seafood, shrimp or octopus, marinated in fresh lime juice, served with red onions, Cusco corn and sweet potatoes<br>Pescado – $15.95<br>Camaron – $17.95<br>Mixto – $17.95<br>Camaron con Pulpo – $19.95</p>
    </div>
  </section>
  <div class="dish-photo dish-photo--ceviche" role="img" aria-label="Photo of a shrimp and fish ceviche plate" style="left:22px;top:752px;width:120px;height:120px;"></div>

  <!-- Panel two -->
  <section class="menu-card" style="left:461px;top:31px;width:290px;height:409px;">
    <h2 class="section-title">Del Mar<br>/ Seafood</h2>
    <p class="dish-name">Pescado a lo Macho</p>
    <p class="dish-desc">fried fish fillet topped with seafood in hot yellow pepper sauce, served with rice and yuccas – $19.95</p>
    <p class="dish-name">Pescado Sudado</p>
    <p class="dish-desc">corvina fish stew, in hot yellow pepper, tomatoes, onions, served with yuccas and rice – $16.95</p>
    <p class="dish-name">Arroz con Mariscos</p>
    <p class="dish-desc">peruvian style paella, red rice served with seafood – $17.95</p>
    <p class="dish-name">Arroz Chaufa</p>
    <p class="dish-desc">peruvian style fried rice served with choice of seafood or shrimp<br>Mariscos – $17.95 &nbsp; Camarones – $17.95</p>
    <p class="dish-name">Trucha Frita</p>
    <p class="dish-desc">deep fried Trout, served with white rice, fried yuccas and salsa criolla – $18.95</p>
    <p class="dish-name">Jalea</p>
    <p class="dish-desc narrow">deep fried mixed seafood and fish, served with fried yuccas<br>Large – $28.95<br>Small – $17.95</p>
  </section>
  <div class="dish-photo dish-photo--seafood" role="img" aria-label="Photo of a fried fish fillet with rice" style="left:640px;top:385px;width:120px;height:120px;"></div>

  <section class="menu-card" style="left:461px;top:513px;width:290px;height:361px;">
    <h2 class="section-title">Pollo a la Brasa<br>/Chicken</h2>
    <p class="dish-name">1/4 Pollo</p>
    <p class="dish-desc">quarter chicken, served with two sides – $6.50</p>
    <p class="dish-name">1/2 Pollo</p>
    <p class="dish-desc">half chicken, served with two sides – $8.95</p>
    <p class="dish-name">1 Pollo</p>
    <p class="dish-desc">whole chicken, served with two sides – $16.95</p>
    <p class="dish-name">Pollo Limeño</p>
    <p class="dish-desc">whole chicken, served with French fries, avocado salad and yellow rice – $20.95</p>
    <p class="dish-name">Pollo Chalaco</p>
    <p class="dish-desc narrow">whole chicken, served with avocado salad, salchipapa and yellow rice – $26.95</p>
    <p class="dish-name">Pollo Tamaru</p>
    <p class="dish-desc narrow">whole chicken, served with avocado salad, arroz chaufa (chicken or steak) and salchipapa – $30.95</p>
  </section>
  <div class="dish-photo dish-photo--chicken" role="img" aria-label="Photo of rotisserie chicken plates with sides" style="left:640px;top:742px;width:130px;height:130px;"></div>

  <!-- Panel three -->
  <section class="menu-card" style="left:854px;top:64px;width:290px;height:791px;padding-top:16px;">
    <h2 class="section-title title-right" style="font-size:19px;margin-bottom:22px;margin-left:80px;">Lo Mas Crillo<br>/ Traditional Dishes</h2>
    <p class="dish-name">Parrillada Mixta</p>
    <p class="dish-desc">dish combined of grilled NY Strip steak, anticuchos (Peruvian style kebabs), pork chops and sausage – $30.95</p>
    <p class="dish-name">Churrasco en Salsa de Camarones</p>
    <p class="dish-desc">NY Strip steak topped with shrimps on hot yellow pepper sauce, served with rice – $20.95</p>
    <p class="dish-name">Seco Norteño</p>
    <p class="dish-desc">slowly cooked lamb stew in aji panka sauce, served with rice and Peruvian canario beans – $20.95</p>
    <p class="dish-name">Seco de Pato Piurano</p>
    <p class="dish-desc">slowly cooked duck stew in aji panka sauce, served with rice and hard-boiled yuccas – $17.95</p>
    <p class="dish-name">Tallarines Verdes con Churrasco</p>
    <p class="dish-desc">linguine pasta in Peruvian style pesto sauce served with grilled NY Strip steak – $18.95</p>
    <p class="dish-name">Tacu Tacu</p>
    <p class="dish-desc">peruvian canario beans mixed with rice, served with choice of NY Strip steak or wok-seared beef in soy sauce<br>Churrasco – $18.95 &nbsp; Lomo – $15.95</p>
    <p class="dish-name">Churrasco a lo Pobre</p>
    <p class="dish-desc">NY Strip steak served with fried eggs, sweet plantains, French fries and rice – $19.95</p>
    <p class="dish-name">Saltado</p>
    <p class="dish-desc">choice of wok-seared steak or chicken, mixed with red onions, tomatoes, in soy sauce, served with French fries and rice<br>Lomo – $15.95 &nbsp; Pollo – $13.95</p>
    <p class="dish-name">Aeropuerto</p>
    <p class="dish-desc">peruvian style fried rice, mixed with noodles, chicken, beef and shrimp – $18.95</p>
    <p class="dish-name">Arroz Chaufa</p>
    <p class="dish-desc">peruvian style fried rice mixed with choice of beef or chicken<br>Carne – $14.95 &nbsp; Pollo – $12.95</p>
    <p class="dish-name">Seco de Carne</p>
    <p class="dish-desc">beef ribs stew in aji panka sauce, served with rice and Peruvian canario beans – $15.95</p>
    <p class="dish-name">Aji de Gallina</p>
    <p class="dish-desc">shredded chicken in a spicy aji amarillo creamy sauce, hard-boiled eggs, olives, potatoes and rice – $11.95</p>
  </section>
  <div class="dish-photo dish-photo--steak" role="img" aria-label="Photo of a traditional beef dish with rice" style="left:818px;top:10px;width:130px;height:130px;"></div>
</main>
</body>
</html>
```